Township of Quenford E-Alert Signup

Need to create print media that is designed for a Town in New Jersey that is starting a marketing campaign to get townspeople to sign up for the E-Alert system.Need print media that is 1. interchangeable in size (regular letter-size, as well as a poster size) 2. Branded with their colors, logo, etc. (green and white displayed in logo)3. Displays the incentives to sign up. Incentives:- Community Services/Announcements- Gov’t/Non-profit Resources- Tax Information- Employment opportunities- Municipal Services/Public Works/Recreation Divisions- Health Updates
Target Market(s)
Townspeople of Maplewood NJ
Industry/Entity Type
Government
Colors
Designer to choose colors to be used in the design.
Requirements
Must have
- 1. interchangeable in size (regular letter-size, as well as a poster size)
- 2. Branded with their colors, logo, etc. (green and white displayed in logo)
- 3. Displays the incentives to sign up.
- Incentives:
- - Community Services/Announcements
- - Gov’t/Non-profit Resources
- - Tax Information
- - Employment opportunities
- - Municipal Services/Public Works/Recreation Divisions
- - Health Updates

```html
<!DOCTYPE html>
<html lang="en">
<head>
<meta charset="utf-8">
<title>Township of Quenford E-Alert Signup</title>
<link rel="stylesheet" href="https://fonts.googleapis.com/css2?family=Lato:wght@300&family=Cabin:ital,wght@1,400&family=Montserrat:wght@800&display=swap">
<style>
  :root {
    --backdrop: #e1efe5;
    --paper: #ffffff;
    --green-dark: #3f7a3f;
    --green-mid: #5a9a46;
    --green-light: #96c34a;
    --photo-light: #a9cfa6;
    --photo-deep: #5f9a63;
    --shadow-grey: #d9dbd9;
  }
  html, body {
    margin: 0;
    width: 986px;
    height: 1200px;
    overflow: hidden;
    background: var(--backdrop);
  }
  .flyer {
    position: absolute;
    left: 129px;
    top: 129px;
    width: 729px;
    height: 943px;
    background: var(--paper);
  }
  .flyer svg { display: block; width: 100%; height: 100%; }
  .title {
    font-family: "Lato", "Gill Sans", sans-serif;
    font-weight: 300;
    font-size: 98px;
    fill: var(--paper);
  }
  .badge-text {
    font-family: "Montserrat", "Arial Black", sans-serif;
    font-weight: 800;
    font-size: 90px;
    fill: var(--green-dark);
    letter-spacing: -2px;
  }
  .incentive {
    font-family: "Cabin", "Gill Sans", sans-serif;
    font-style: italic;
    font-size: 38px;
    fill: var(--green-dark);
  }
</style>
</head>
<body>
<main class="flyer">
  <svg viewBox="0 0 1283 1661" xmlns="http://www.w3.org/2000/svg">
    <defs>
      <linearGradient id="band-gradient" x1="0" x2="1" y1="0" y2="0">
        <stop offset="0" stop-color="var(--green-light)"/>
        <stop offset="0.65" stop-color="var(--green-mid)"/>
        <stop offset="1" stop-color="var(--green-dark)"/>
      </linearGradient>
      <linearGradient id="street-gradient" x1="0" x2="0" y1="0" y2="1">
        <stop offset="0" stop-color="var(--photo-light)"/>
        <stop offset="0.6" stop-color="var(--photo-deep)"/>
        <stop offset="1" stop-color="var(--photo-light)"/>
      </linearGradient>
      <radialGradient id="park-gradient" cx="0.5" cy="0.5" r="0.6">
        <stop offset="0" stop-color="#5f9a63"/>
        <stop offset="1" stop-color="#2f6a38"/>
      </radialGradient>
      <clipPath id="flyer-clip"><rect width="1283" height="1661"/></clipPath>
    </defs>

    <g clip-path="url(#flyer-clip)">
      <!-- Street photo panel -->
      <path class="street-photo" role="img" aria-label="Photo of a historic main street with shops and tudor-style buildings, tinted green"
            d="M0 0 H650 C720 170 770 380 735 560 C650 790 380 900 0 918 Z"
            fill="url(#street-gradient)"/>
      <path d="M650 0 C720 170 770 380 735 560 C650 790 380 900 0 918"
            fill="none" stroke="var(--green-dark)" stroke-width="5"/>
      <path d="M735 560 C650 790 380 900 0 918" fill="none" stroke="var(--green-light)" stroke-width="4"/>

      <!-- Title band -->
      <path d="M425 275 H1283" stroke="var(--green-dark)" stroke-width="4"/>
      <path d="M545 620 H1283" stroke="var(--green-dark)" stroke-width="4"/>
      <path d="M425 275 L528 620" stroke="var(--green-dark)" stroke-width="4"/>
      <polygon points="440,288 1283,288 1283,607 536,607" fill="url(#band-gradient)"/>
      <text class="title" x="530" y="416">TOWNSHIP OF</text>
      <text class="title" x="530" y="502">QUENFORD</text>

      <!-- E-Alert badge -->
      <g transform="translate(820 630) rotate(-12)">
        <rect x="-222" y="-82" width="456" height="196" rx="34" fill="var(--shadow-grey)"/>
        <rect x="-232" y="-98" width="456" height="196" rx="34" fill="var(--paper)" stroke="var(--green-dark)" stroke-width="16"/>
        <text class="badge-text" x="-200" y="-8">E-ALERT</text>
        <text class="badge-text" x="-200" y="76">SIGNUP</text>
      </g>

      <!-- Pointer hand icon -->
      <g transform="translate(985 680) rotate(-12)" fill="var(--green-dark)">
        <rect x="-8" y="0" width="22" height="70" rx="11"/>
        <path d="M-8 55 L-30 40 C-44 32 -54 46 -44 56 L-4 110 H66 C74 90 76 70 70 50 C68 40 56 38 50 46 C50 34 38 32 32 40 C30 28 16 28 14 36 V55 Z"/>
      </g>

      <!-- Incentives -->
      <g class="incentive">
        <circle cx="541" cy="909" r="6" fill="var(--green-dark)"/>
        <text x="573" y="921">Community Services/Announcements</text>
        <circle cx="541" cy="970" r="6" fill="var(--green-dark)"/>
        <text x="573" y="982">Gov’t/Non-profit Resources</text>
        <circle cx="541" cy="1030" r="6" fill="var(--green-dark)"/>
        <text x="573" y="1042">Tax Information</text>
        <circle cx="541" cy="1090" r="6" fill="var(--green-dark)"/>
        <text x="573" y="1102">Employment opportunities</text>
        <circle cx="541" cy="1151" r="6" fill="var(--green-dark)"/>
        <text x="573" y="1163">Municipal Services/Public Works/</text>
        <text x="573" y="1213">Recreation Divisions</text>
        <circle cx="541" cy="1263" r="6" fill="var(--green-dark)"/>
        <text x="573" y="1275">Health Updates</text>
      </g>

      <!-- Aerial park photo -->
      <circle cx="1093" cy="1575" r="309" fill="none" stroke="var(--green-mid)" stroke-width="3"/>
      <circle class="park-photo" role="img" aria-label="Aerial photo of a town green with crossing paths and trees, tinted green"
              cx="1093" cy="1575" r="300" fill="url(#park-gradient)"/>
    </g>
  </svg>
</main>
</body>
</html>
```